Business Card Design Project

We are looking to redesign the logo, business card and stationary of one of our group companies - KESTRAL SUPPLY COMPANY LLC.

The company specialises in industrial PVC and CPVC Piping systems. It is situated in the Middle East and the focus is purely in this region.

The logo work is already completed. The file is uploaded for the reference.

We are looking for a clean minimalistic design for the business card.

regards
Ormund
Updates

Hello Everyone!

Thanks for submitting your designs. 

Yet to find the right design. Probably the below links will give you guys some more idea on what we would like.

Minimalist design with some creativity.

Ormund

http://plaincardgallery.example/inspiration/15-beautifully-minimal-business-cards

http://www.quietlayouthub.example/2011/11/14/30-minimalist-business-card-design/

http://www.firmpixelnotes.example/inspiration/minimal-business-cards/

Target Market(s)

Industrial users

Industry/Entity Type

Industrial

Requirements
Must have
• - Minimalistic design

- Back side of the card should include the manufacturer BRAVOLINE CANADA's decal. The file is upload for the reference

- Further information
Company Name:
KESTRAL SUPPLY COMPANY LLC
Address:
PO Box 9087, Sharjah Industrial Area 5, Qutrani Road
Sharjah, United Arab Emirates
Telephone:
+971-6-5018-392
Fax:
+977-6-5018-393
Email:
mail@ksc-holding.example

- FYI, Kestral Supply Company LLC is the authorised distributor for BRAVOLINE CANADA in the UAE. For further information on bravoline please visit the website www.bravoline.example

```html
<!DOCTYPE html>
<html lang="en">
<head>
<meta charset="utf-8">
<title>Kestral Supply Company – Business Card</title>
<link href="https://fonts.googleapis.com/css2?family=Questrial&family=Open+Sans:wght@600;700&display=swap" rel="stylesheet">
<style>
  :root {
    --bg-centre: #0f2d4c;
    --bg-mid: #061a2f;
    --bg-edge: #01050c;
    --brand-blue: #6fa3dc;
    --text-white: #ffffff;
    --mark-fill: #4a86cf;
    --partner-square: #0a0a0a;
  }
  html, body {
    margin: 0;
    padding: 0;
    overflow: hidden;
    background: var(--bg-edge);
  }
  .card {
    position: relative;
    width: 1200px;
    height: 720px;
    overflow: hidden;
    background: radial-gradient(ellipse 62% 70% at 50% 40%, var(--bg-centre) 0%, var(--bg-mid) 55%, var(--bg-edge) 100%);
  }
  .brand-square {
    position: absolute;
    left: 542px;
    top: 212px;
    width: 88px;
    height: 88px;
    border-radius: 22px;
    background: var(--mark-fill);
  }
  .company-name {
    position: absolute;
    left: 0;
    width: 1200px;
    top: 314px;
    margin: 0;
    text-align: center;
    font-family: "Questrial", sans-serif;
    font-weight: 400;
    font-size: 46px;
    letter-spacing: 0.5px;
    color: var(--brand-blue);
  }
  .product-line {
    position: absolute;
    left: 0;
    width: 1200px;
    top: 380px;
    margin: 0;
    text-align: center;
    font-family: "Open Sans", sans-serif;
    font-weight: 600;
    font-size: 20px;
    letter-spacing: 1.6px;
    color: var(--text-white);
  }
  .product-line .divider {
    margin: 0 8px;
    font-weight: 400;
  }
  .partner {
    position: absolute;
    left: 899px;
    top: 572px;
    display: flex;
    align-items: center;
    gap: 10px;
  }
  .partner-square {
    width: 56px;
    height: 56px;
    background: var(--partner-square);
  }
  .partner-name {
    font-family: "Open Sans", sans-serif;
    font-weight: 700;
    font-size: 25px;
    line-height: 27px;
    color: var(--text-white);
  }
</style>
</head>
<body>
  <main class="card">
    <div class="brand-square" aria-hidden="true"></div>
    <h1 class="company-name">KESTRAL SUPPLY COMPANY</h1>
    <p class="product-line">PIPES<span class="divider">|</span>FITTINGS<span class="divider">|</span>VALVES<span class="divider">|</span>ACCESSORIES</p>
    <div class="partner">
      <div class="partner-square" aria-hidden="true"></div>
      <div class="partner-name">Bravoline<br>Canada</div>
    </div>
  </main>
</body>
</html>
```